Business cards

I would like a black background with the design I previously chose. I need 2 sets of cards. Mine will have Marisol Brandt, Broker/Owner, 307-555-0148 and marisol.harborpeak@mailvista.com
The second set will read, Dana Rutledge, Realtor 307-555-0172, dana.harborpeak@mailvista.com

Industry/Entity Type

Business

```html
<!DOCTYPE html>
<html lang="en">
<head>
<meta charset="utf-8">
<title>Business Cards – Marisol Brandt &amp; Dana Rutledge</title>
<link rel="stylesheet" href="https://fonts.googleapis.com/css2?family=Tinos:wght@700&family=Open+Sans:wght@400&display=swap">
<style>
  :root {
    --page-bg: #e9e7e3;
    --card-border: #ffffff;
    --card-face: #0b0b0c;
    --card-sheen: #2a2b2d;
    --ink-light: #f4f4f4;
  }
  html, body {
    margin: 0;
    padding: 0;
    width: 1200px;
    height: 1200px;
    overflow: hidden;
    background: var(--page-bg);
  }
  .canvas {
    width: 1200px;
    height: 1200px;
    display: flex;
    flex-direction: column;
    align-items: center;
    justify-content: center;
    gap: 56px;
  }
  .business-card {
    width: 860px;
    height: 492px;
    box-sizing: border-box;
    padding: 24px;
    background: var(--card-border);
    box-shadow: 0 16px 36px rgba(0,0,0,0.18);
    flex: none;
  }
  .card-face {
    width: 100%;
    height: 100%;
    background: linear-gradient(115deg, var(--card-face) 0%, var(--card-face) 22%, var(--card-sheen) 34%, var(--card-face) 48%, var(--card-face) 100%);
    display: flex;
    flex-direction: column;
    align-items: center;
    justify-content: center;
    color: var(--ink-light);
    text-align: center;
  }
  .holder-name {
    font-family: "Tinos", "Times New Roman", serif;
    font-weight: 700;
    font-size: 50px;
    letter-spacing: 0.5px;
    text-transform: uppercase;
    margin: 0;
    line-height: 1;
  }
  .holder-title {
    font-family: "Open Sans", Arial, sans-serif;
    font-size: 24px;
    margin: 12px 0 0;
  }
  .contact-list {
    list-style: none;
    padding: 0;
    margin: 38px 0 0;
    font-family: "Open Sans", Arial, sans-serif;
    font-size: 28px;
    line-height: 1.55;
  }
</style>
</head>
<body>
  <main class="canvas">
    <article class="business-card card-broker">
      <div class="card-face">
        <h1 class="holder-name">Marisol Brandt</h1>
        <p class="holder-title">Broker/Owner</p>
        <ul class="contact-list">
          <li class="contact-phone">T: 307-555-0148</li>
          <li class="contact-email">E: marisol.harborpeak@mailvista.com</li>
        </ul>
      </div>
    </article>
    <article class="business-card card-realtor">
      <div class="card-face">
        <h2 class="holder-name">Dana Rutledge</h2>
        <p class="holder-title">Realtor</p>
        <ul class="contact-list">
          <li class="contact-phone">T: 307-555-0172</li>
          <li class="contact-email">E: dana.harborpeak@mailvista.com</li>
        </ul>
      </div>
    </article>
  </main>
</body>
</html>
```